To revamp the exting web page and Company presentation to new propsective client

We are company establish in 2006. We have a combine of Veltrix implementation team of more than 10 years. We focus on the following areas

a) Veltrix T-ledger range implementation
b) Veltrix T-ledger range platform migration
c) Large database size in excess of 20TB

We need to redesign a our existing new card to give a new look and refresh look. Kindly visit our website for more info www.bnlzq.com

Your main them is blue color and hope to hear from you all.

Target Market(s)

Professional clients

Industry/Entity Type

Information Technology

Contact Information for Business Card

To market our as the leading Veltrix partner in Veltrix t-ledger range implementation

Number of Pages Required

1 page

Colors
3276b5
9bcb3c
cadf82
33a6d7

Requirements
Must have
• The ability to attract new customer and show a level of professionalism.
• You can also add a green color to represent green and environmental friendly.
Nice to have
• To give a total new fresh look for the company
Should not have
• None

```html
<!DOCTYPE html>
<html lang="en">
<head>
<meta charset="utf-8">
<title>Daniel Ong – Business Card</title>
<link rel="stylesheet" href="https://fonts.googleapis.com/css2?family=Didact+Gothic&family=Lexend:wght@800&display=swap">
<style>
  :root {
    --navy: #0b0b42;
    --blue: #3276b5;
    --lime: #cadf82;
    --paper: #ffffff;
    --ink-light: #f2f3f8;
  }
  html, body {
    margin: 0;
    padding: 0;
    width: 1200px;
    height: 686px;
    overflow: hidden;
    background: var(--paper);
  }
  .card {
    position: relative;
    width: 1200px;
    height: 686px;
    background: var(--paper);
    overflow: hidden;
    font-family: "Didact Gothic", "Century Gothic", sans-serif;
  }
  .card__sweep {
    position: absolute;
    inset: 0;
  }
  .identity {
    position: absolute;
    left: 40px;
    top: 246px;
    width: 476px;
    text-align: center;
    color: var(--navy);
  }
  .identity__name {
    margin: 0;
    font-family: "Lexend", "Century Gothic", sans-serif;
    font-weight: 800;
    font-size: 78px;
    line-height: 1;
    letter-spacing: 1px;
    transform: scaleY(1.05);
  }
  .identity__title {
    margin: 10px 0 0;
    font-size: 26px;
    letter-spacing: 0.5px;
  }
  .brand {
    position: absolute;
    left: 120px;
    top: 606px;
    width: 310px;
    display: flex;
    align-items: center;
    justify-content: center;
    gap: 16px;
    color: var(--navy);
  }
  .brand__dot {
    width: 22px;
    height: 22px;
    border-radius: 50%;
    background: var(--navy);
  }
  .brand__name {
    font-size: 32px;
    letter-spacing: 9px;
    text-transform: uppercase;
  }
  .contacts {
    position: absolute;
    left: 742px;
    top: 64px;
    margin: 0;
    padding: 0;
    list-style: none;
    color: var(--ink-light);
    font-size: 26px;
    line-height: 34px;
  }
  .contact {
    position: absolute;
    left: 0;
    display: flex;
    align-items: flex-start;
    width: 440px;
  }
  .contact__icon {
    flex: none;
    width: 46px;
    height: 46px;
    border-radius: 50%;
    background: var(--lime);
    display: flex;
    align-items: center;
    justify-content: center;
    margin-right: 31px;
  }
  .contact__icon svg { width: 26px; height: 26px; }
  .contact__text { margin-top: 0; }
  .contact--address { top: 0; }
  .contact--phone { top: 201px; }
  .contact--fax { top: 318px; }
  .contact--mobile { top: 400px; }
  .contact--email { top: 506px; }
  .contact--single .contact__text { margin-top: 6px; }
</style>
</head>
<body>
<main class="card">
  <svg class="card__sweep" viewBox="0 0 1200 686" width="1200" height="686" aria-hidden="true">
    <path fill="var(--blue)" d="M526 0 C 548 230, 610 470, 688 686 L1200 686 L1200 0 Z"/>
    <path fill="var(--lime)" d="M622 0 C 622 240, 640 470, 694 686 L1200 686 L1200 0 Z"/>
    <path fill="var(--navy)" d="M709 0 C 650 200, 640 460, 703 686 L1200 686 L1200 0 Z"/>
  </svg>

  <section class="identity">
    <h1 class="identity__name">DANIEL ONG</h1>
    <p class="identity__title">Chief Operating Officer</p>
  </section>

  <div class="brand">
    <span class="brand__dot"></span>
    <span class="brand__name">Norvane</span>
  </div>

  <ul class="contacts">
    <li class="contact contact--address">
      <span class="contact__icon">
        <svg viewBox="0 0 24 24"><path fill="var(--navy)" d="M12 2a7 7 0 0 0-7 7c0 5.2 7 13 7 13s7-7.8 7-13a7 7 0 0 0-7-7zm0 9.6A2.6 2.6 0 1 1 12 6.4a2.6 2.6 0 0 1 0 5.2z"/></svg>
      </span>
      <span class="contact__text">Suite 5.02, 5th floor,<br>Menara Halvex, Seri Tanjung<br>City, Jalan Permai<br>Utama, 50480 Kuala<br>Lumpur, Malaysia</span>
    </li>
    <li class="contact contact--phone">
      <span class="contact__icon">
        <svg viewBox="0 0 24 24"><path fill="var(--navy)" d="M6.6 2.5l3 3.4-1.8 2.6c1.2 2.9 3.6 5.4 6.7 6.8l2.5-1.9 3.5 2.9-1.6 3.5c-7.6.3-15.2-7.4-14.9-15l2.6-2.3z"/></svg>
      </span>
      <span class="contact__text">60 3 5518 7730<br>65 6240 1395 (SG)</span>
    </li>
    <li class="contact contact--fax contact--single">
      <span class="contact__icon">
        <svg viewBox="0 0 24 24"><g fill="none" stroke="var(--navy)" stroke-width="1.8"><rect x="2" y="8" width="5" height="13" rx="1"/><rect x="7" y="10" width="15" height="11" rx="1"/><path d="M10 10V3h8l2 2v5"/></g><g fill="var(--navy)"><rect x="10" y="13" width="2" height="2"/><rect x="14" y="13" width="2" height="2"/><rect x="18" y="13" width="2" height="2"/><rect x="10" y="17" width="2" height="2"/><rect x="14" y="17" width="2" height="2"/><rect x="18" y="17" width="2" height="2"/></g></svg>
      </span>
      <span class="contact__text">60 3 5518 7701</span>
    </li>
    <li class="contact contact--mobile contact--single">
      <span class="contact__icon">
        <svg viewBox="0 0 24 24"><rect x="6.5" y="2" width="11" height="20" rx="2" fill="none" stroke="var(--navy)" stroke-width="1.8"/><line x1="10.5" y1="4.8" x2="13.5" y2="4.8" stroke="var(--navy)" stroke-width="1.4"/><circle cx="12" cy="19" r="1.1" fill="var(--navy)"/></svg>
      </span>
      <span class="contact__text">60 12 846 2051</span>
    </li>
    <li class="contact contact--email contact--single">
      <span class="contact__icon">
        <svg viewBox="0 0 24 24"><g fill="none" stroke="var(--navy)" stroke-width="1.8"><rect x="2.5" y="5" width="19" height="14" rx="1"/><path d="M2.5 5.5l9.5 7.5 9.5-7.5M2.5 18.5l7-6.5M21.5 18.5l-7-6.5"/></g></svg>
      </span>
      <span class="contact__text">danielong@bnlzq.com</span>
    </li>
  </ul>
</main>
</body>
</html>
```